hi all

Im after a new age looking business card with my company logo on it

must include these details, I would like the PH and Email to be symbols

If the colours used for card could be kept within the colours used in logo that I have supplied that would be great, if another colour is to be used dark grey would be ok. no light bulbs etc thanks

Details below to be incorporated on card

Damian Holloway

Lic E871302

PH 0219647381

E info@brightvaleelectrical.example.nz

Domestic Commercial Industrial Electricians

```html
<!DOCTYPE html>
<html lang="en">
<head>
<meta charset="utf-8">
<title>Brightvale Electrical — Business Card</title>
<link href="https://fonts.googleapis.com/css2?family=Jost:wght@300;400;600&display=swap" rel="stylesheet">
<style>
  :root {
    --brand-blue: #2e88c8;
    --logo-blue: #1b74c4;
    --deep-blue: #1f5f8f;
    --ink: #111111;
    --paper: #ffffff;
    --soft-white: #e4eff8;
  }
  * { margin: 0; padding: 0; box-sizing: border-box; }
  html, body {
    width: 1200px;
    height: 693px;
    overflow: hidden;
    background: var(--paper);
  }
  .card {
    position: relative;
    width: 1200px;
    height: 693px;
    background: var(--paper);
    font-family: "Jost", "Futura", sans-serif;
  }
  .brand-panel {
    position: absolute;
    left: 0; top: 0;
    width: 428px; height: 693px;
    background: var(--paper);
  }
  .brand-name {
    position: absolute;
    left: 60px; top: 296px;
    width: 300px;
    color: var(--logo-blue);
    font-weight: 600;
    text-align: center;
    line-height: 1.05;
  }
  .brand-name .line-main {
    display: block;
    font-size: 42px;
    letter-spacing: 1px;
  }
  .brand-name .line-sub {
    display: block;
    font-size: 15px;
    letter-spacing: 5px;
    text-align: right;
    padding-right: 2px;
  }
  .contact-panel {
    position: absolute;
    left: 428px; top: 0;
    width: 772px; height: 693px;
    background: var(--brand-blue);
  }
  .divider {
    position: absolute;
    left: 0; top: 562px;
  }
  .holder-name {
    position: absolute;
    left: 612px; top: 248px;
    width: 560px;
    color: var(--paper);
    font-size: 61px;
    font-weight: 400;
    line-height: 1;
    white-space: nowrap;
  }
  .licence {
    position: absolute;
    left: 616px; top: 316px;
    width: 552px;
    display: flex;
    justify-content: space-between;
    color: var(--soft-white);
    font-size: 24px;
    font-weight: 300;
    line-height: 1;
  }
  .licence .label { letter-spacing: 20px; }
  .licence .number { letter-spacing: 19px; margin-right: -19px; }
  .contact-row {
    position: absolute;
    left: 614px;
    display: flex;
    align-items: center;
    gap: 10px;
    color: var(--soft-white);
    font-weight: 300;
    white-space: nowrap;
    line-height: 1;
  }
  .contact-row.phone { top: 598px; font-size: 30px; }
  .contact-row.email { top: 640px; font-size: 26px; }
  .icon { flex: none; display: block; }
</style>
</head>
<body>
  <main class="card">
    <section class="brand-panel">
      <div class="brand-name">
        <span class="line-main">BRIGHTVALE</span>
        <span class="line-sub">ELECTRICAL</span>
      </div>
    </section>

    <section class="contact-panel"></section>

    <svg class="divider" width="1200" height="16" viewBox="0 0 1200 16" aria-hidden="true">
      <line x1="0" y1="8" x2="179" y2="8" stroke="var(--ink)" stroke-width="1.3"/>
      <circle cx="185" cy="8" r="5.5" fill="var(--paper)" stroke="var(--ink)" stroke-width="1.3"/>
      <circle cx="242" cy="8" r="5.5" fill="var(--paper)" stroke="var(--ink)" stroke-width="1.3"/>
      <line x1="248" y1="8" x2="428" y2="8" stroke="var(--ink)" stroke-width="1.3"/>
      <line x1="428" y1="8" x2="1200" y2="8" stroke="var(--paper)" stroke-width="1.3"/>
    </svg>

    <h1 class="holder-name">Damian Holloway</h1>
    <p class="licence"><span class="label">Lic</span><span class="number">E871302</span></p>

    <p class="contact-row phone">
      <svg class="icon" width="30" height="30" viewBox="0 0 30 30" aria-label="Phone">
        <rect x="0" y="0" width="30" height="30" rx="5" fill="var(--deep-blue)"/>
        <path d="M9 7.5c1-.8 2-.6 2.6.3l1.6 2.5c.5.8.3 1.6-.4 2.1l-1 .7c.8 2 2.4 3.8 4.4 4.9l.8-1c.6-.7 1.4-.8 2.1-.3l2.5 1.7c.8.6.9 1.6.2 2.5l-1 1.2c-.8 1-2.2 1.3-3.6.7-4.6-2-8-5.6-9.6-10.2-.5-1.4-.1-2.8.9-3.6z" fill="var(--paper)"/>
      </svg>
      <span>0219647381</span>
    </p>

    <p class="contact-row email">
      <svg class="icon" width="34" height="24" viewBox="0 0 34 24" aria-label="Email">
        <rect x="1" y="1" width="32" height="22" rx="2" fill="none" stroke="var(--deep-blue)" stroke-width="1.8"/>
        <path d="M1.5 2l15.5 12 15.5-12M1.5 22l12-10M32.5 22l-12-10" fill="none" stroke="var(--deep-blue)" stroke-width="1.8"/>
      </svg>
      <span>info@brightvaleelectrical.example.nz</span>
    </p>
  </main>
</body>
</html>
```